Exciting & Elegant Stationary Pack

Stationary consists of
1. Letter head / Envelope
2. Business Card
3. Invoice
4. 40x40mm sticker

Attached files;

1. Logo (Other formats available on request)
2. MS word Doc - For information and description of design
3. Website image (This will be our new website so use the colours so everything ties together)
4. Sample of stationary pack we like, but feel free to be creative

Target Market(s)

Home improvement

Industry/Entity Type

Construction

Font styles to use
Other font styles liked:
• Leave up to designer - We like font used on (website attached image)

Requirements
Must have
• Please look at uploaded file of sample website and use colours
Nice to have
• Any type of business card design - eg. metal, die cut, embossed, etc...

```html
<!DOCTYPE html>
<html lang="en">
<head>
<meta charset="utf-8">
<title>Grout &amp; Level — Stationery Pack</title>
<link rel="stylesheet" href="https://fonts.googleapis.com/css2?family=Open+Sans:wght@400;600;800&family=Arimo:wght@400&family=Tinos:wght@400&display=swap">
<style>
  :root {
    --red: #c1272d;
    --blue-text: #2e7fc2;
    --navy: #0e3f66;
    --sky: #9dc0e3;
    --paper: #ffffff;
    --ink: #2b2b2b;
  }
  * { box-sizing: border-box; margin: 0; padding: 0; }
  html, body { width: 1200px; height: 1119px; overflow: hidden; background: var(--paper); }
  body { position: relative; font-family: "Open Sans", Arial, sans-serif; }

  .sheet { position: absolute; background: var(--paper); box-shadow: 3px 4px 8px rgba(0,0,0,.28); overflow: hidden; }

  .brand-name { color: var(--red); font-weight: 600; letter-spacing: .2px; white-space: nowrap; }
  .abn { color: var(--blue-text); white-space: nowrap; }
  .abn span { color: var(--red); }
  .wordmark { position: absolute; color: var(--navy); font-weight: 800; line-height: 1; white-space: nowrap; text-align: right; }

  /* Letterhead */
  .letterhead { left: 47px; top: 39px; width: 518px; height: 676px; }
  .letterhead .brand-name { position: absolute; left: 47px; top: 52px; font-size: 17px; }
  .letterhead .abn { position: absolute; left: 47px; top: 74px; font-size: 13px; }
  .letterhead .wordmark { right: 38px; top: 30px; font-size: 22px; }
  .letterhead .rule { position: absolute; left: 0; top: 105px; width: 100%; height: 14px; background: var(--red); }
  .letter-body { position: absolute; left: 52px; top: 163px; width: 290px; font-family: "Arimo", Arial, sans-serif; font-size: 7.2px; line-height: 10.4px; color: var(--ink); }
  .letter-body p { margin-bottom: 10px; }
  .letter-body .date { margin: 16px 0 26px; }
  .letter-sign { position: absolute; left: 52px; top: 486px; font-family: "Tinos", "Times New Roman", serif; font-size: 7.5px; line-height: 10px; color: var(--ink); }
  .signature { display: block; width: 108px; height: 20px; margin: 4px 0 0 6px; background: linear-gradient(90deg, #5a5a5a, #2b2b2b); border-radius: 10px; opacity: .55; }
  .letter-sign .cc { margin-top: 22px; }
  .letter-sign .cc span { display: block; padding-left: 16px; }
  .letter-footer { position: absolute; left: 22px; right: 22px; top: 618px; display: flex; justify-content: space-between; font-size: 9.5px; color: #333; }
  .letter-footer .item { display: flex; align-items: center; gap: 5px; white-space: nowrap; }
  .letter-footer svg, .card-contacts svg { width: 10px; height: 10px; fill: var(--red); flex: none; }
  .letterhead .base { position: absolute; left: 0; bottom: 0; width: 100%; height: 32px; background: var(--sky); }

  /* Folder */
  .folder { left: 640px; top: 37px; width: 523px; height: 676px; background: var(--sky); }
  .folder .heading { position: absolute; right: 34px; top: 32px; text-align: right; color: #eef5fc; }
  .folder .heading .name { font-size: 20px; font-weight: 400; letter-spacing: .4px; }
  .folder .heading .abn { color: #eef5fc; font-size: 15px; margin-top: 2px; }
  .folder .wordmark { left: 50px; top: 455px; font-size: 66px; color: var(--paper); text-align: left; }

  /* Business card */
  .card { left: 44px; top: 805px; width: 461px; height: 252px; }
  .card .band { position: absolute; left: 0; top: 0; width: 100%; height: 57px; background: var(--sky); }
  .card .brand-name { position: absolute; left: 30px; top: 102px; font-size: 17px; }
  .card .abn { position: absolute; left: 30px; top: 125px; font-size: 13px; }
  .card-contacts { position: absolute; left: 26px; top: 176px; list-style: none; font-size: 13px; line-height: 21px; color: #333; }
  .card-contacts li { display: flex; align-items: center; gap: 9px; white-space: nowrap; }
  .card .wordmark { right: 50px; top: 152px; font-size: 20px; }

  /* Envelope */
  .envelope { left: 599px; top: 746px; width: 564px; height: 331px; }
  .envelope .flap { position: absolute; left: 0; top: 0; width: 100%; height: 49px; }
  .envelope .brand-name { position: absolute; left: 34px; top: 82px; font-size: 17px; }
  .envelope .abn { position: absolute; left: 34px; top: 106px; font-size: 13px; }
  .envelope .wordmark { right: 48px; top: 185px; font-size: 20px; }
  .envelope .rule { position: absolute; left: 0; top: 265px; width: 100%; height: 11px; background: var(--red); }
  .envelope .base { position: absolute; left: 0; top: 276px; width: 100%; bottom: 0; background: var(--sky); }
</style>
</head>
<body>

<section class="sheet letterhead" aria-label="Letterhead">
  <div class="brand-name">GROUT &amp; LEVEL</div>
  <div class="abn"><span>ABN</span> 12 345 678 901</div>
  <div class="wordmark">GROUT &amp;<br>LEVEL</div>
  <div class="rule"></div>

  <div class="letter-body">
    <p>Mr Recipient Name<br>Street Address Line<br>City, Region Post Code</p>
    <p class="date">City, Day Month Year</p>
    <p>Dear Recipient Name,</p>
    <p>Thank you for choosing our team for your recent tiling project. We are pleased to confirm the details of the work agreed during our visit. All materials will be supplied and delivered before the start date. Our crew will arrive early each morning and leave the site clean and safe at the end of every day.</p>
    <p>Please review the attached quote and let us know if any changes are needed. Floor and wall tiles can be viewed at our showroom by appointment. We recommend sealing all grout lines within two weeks of completion to keep the finish looking new for years.</p>
    <p>Payment terms are fourteen days from the date of invoice. A deposit secures your booking in our schedule. Should you have any questions about the job, the timeline or the care of your new surfaces, please call our office and we will be glad to help you.</p>
  </div>

  <div class="letter-sign">
    <div>Sincerely,</div>
    <span class="signature" role="img" aria-label="Handwritten signature"></span>
    <div>Daniel Hartley</div>
    <div>Deputy Assistant Director</div>
    <div class="cc">Cc: J. Moreno<span>L. Carter</span></div>
  </div>

  <div class="letter-footer">
    <div class="item">
      <svg viewBox="0 0 10 10" aria-hidden="true"><path d="M5 0a3.6 3.6 0 0 0-3.6 3.6C1.4 6.3 5 10 5 10s3.6-3.7 3.6-6.4A3.6 3.6 0 0 0 5 0zm0 5a1.4 1.4 0 1 1 0-2.8A1.4 1.4 0 0 1 5 5z"/></svg>
      PO BOX 48 RIVERVALE NSW 2150
    </div>
    <div class="item">
      <svg viewBox="0 0 10 10" aria-hidden="true"><path d="M5 0a5 5 0 1 0 0 10A5 5 0 0 0 5 0zm3.9 4.4H7.2a8 8 0 0 0-.6-3 4 4 0 0 1 2.3 3zM5 1.1c.5.7.9 1.9 1 3.3H4c.1-1.4.5-2.6 1-3.3zM3.4 1.4a8 8 0 0 0-.6 3H1.1a4 4 0 0 1 2.3-3zM1.1 5.6h1.7a8 8 0 0 0 .6 3 4 4 0 0 1-2.3-3zM5 8.9c-.5-.7-.9-1.9-1-3.3h2c-.1 1.4-.5 2.6-1 3.3zm1.6-.3a8 8 0 0 0 .6-3h1.7a4 4 0 0 1-2.3 3z"/></svg>
      WWW.GROUTANDLEVEL.COM.AU
    </div>
    <div class="item">
      <svg viewBox="0 0 10 10" aria-hidden="true"><path d="M2.5 0h5a1 1 0 0 1 1 1v8a1 1 0 0 1-1 1h-5a1 1 0 0 1-1-1V1a1 1 0 0 1 1-1zm.2 1.3v6.2h4.6V1.3zM5 8.2a.5.5 0 1 0 0 1 .5.5 0 0 0 0-1z"/></svg>
      0400 123 987
    </div>
  </div>
  <div class="base"></div>
</section>

<section class="sheet folder" aria-label="Presentation folder">
  <div class="heading">
    <div class="name">GROUT &amp; LEVEL</div>
    <div class="abn">ABN 12 345 678 901</div>
  </div>
  <div class="wordmark">GROUT &amp;<br>LEVEL</div>
</section>

<section class="sheet card" aria-label="Business card">
  <div class="band"></div>
  <div class="brand-name">GROUT &amp; LEVEL</div>
  <div class="abn">ABN 12 345 678 901</div>
  <ul class="card-contacts">
    <li>
      <svg viewBox="0 0 10 10" aria-hidden="true"><path d="M2.5 0h5a1 1 0 0 1 1 1v8a1 1 0 0 1-1 1h-5a1 1 0 0 1-1-1V1a1 1 0 0 1 1-1zm.2 1.3v6.2h4.6V1.3zM5 8.2a.5.5 0 1 0 0 1 .5.5 0 0 0 0-1z"/></svg>
      0400 123 987
    </li>
    <li>
      <svg viewBox="0 0 10 10" aria-hidden="true"><path d="M5 0a5 5 0 1 0 0 10A5 5 0 0 0 5 0zm3.9 4.4H7.2a8 8 0 0 0-.6-3 4 4 0 0 1 2.3 3zM5 1.1c.5.7.9 1.9 1 3.3H4c.1-1.4.5-2.6 1-3.3zM3.4 1.4a8 8 0 0 0-.6 3H1.1a4 4 0 0 1 2.3-3zM1.1 5.6h1.7a8 8 0 0 0 .6 3 4 4 0 0 1-2.3-3zM5 8.9c-.5-.7-.9-1.9-1-3.3h2c-.1 1.4-.5 2.6-1 3.3zm1.6-.3a8 8 0 0 0 .6-3h1.7a4 4 0 0 1-2.3 3z"/></svg>
      www.groutandlevel.com.au
    </li>
    <li>
      <svg viewBox="0 0 10 10" aria-hidden="true"><path d="M0 2h10v6H0z"/></svg>
      info@groutandlevel.com.au
    </li>
  </ul>
  <div class="wordmark">GROUT &amp;<br>LEVEL</div>
</section>

<section class="sheet envelope" aria-label="Envelope">
  <svg class="flap" viewBox="0 0 564 49" preserveAspectRatio="none" aria-hidden="true">
    <polygon points="20,0 544,0 564,49 0,49" fill="var(--navy)"/>
  </svg>
  <div class="brand-name">GROUT &amp; LEVEL</div>
  <div class="abn">ABN 12 345 678 901</div>
  <div class="wordmark">GROUT &amp;<br>LEVEL</div>
  <div class="rule"></div>
  <div class="base"></div>
</section>

</body>
</html>
```